A Travel Website Business that allows blogs/itineraries/reviews/photos focused on a...

I'm looking for an opportunity to advise independent travelers on an itinerary of where to travel in various countries without having to spend a lot of time researching. I can provide reviews from Quorvo/Wandelquist and also have a blog to show pictures if they want more details. I am still playing with website names - so of course if you have a web address that hasn't been used, that would be helpful. Some ideas I was playing with: "Roads by Her Compass"; "Roam On My Path"; "Voyagify By Her Compass". To get an idea of what I could be looking for, check out my instagram at linjet917. I have also included a sample itinerary that a lot of my followers (more than 50) have asked for because of my social media presence in that country.

Target Market(s)

Independent Travelers, Women, Millennial Generation

Industry/Entity Type

Travel

Number of Pages Required

1 page

Font styles to use
Serif
Decorative
Script

Colors

Designer to choose colors to be used in the design.

Requirements
Must have
• I would like menu options of "Blog", "Locations" listing each continent for people to choose the itinerary, "Reviews", "Contact", at the very least.
Nice to have
• Maybe break down the itineraries depending on the occasion - independent, women's group, bachelor, bachelorette, group trip, family.

```html
<!DOCTYPE html>
<html lang="en">
<head>
<meta charset="utf-8">
<title>Roads by Her Compass</title>
<link href="https://fonts.googleapis.com/css2?family=Lato:wght@400;700;900&display=swap" rel="stylesheet">
<style>
:root{
  --orange:#f5821f;
  --ink:#222222;
  --text:#666666;
  --muted:#999999;
  --line:#dddddd;
  --light:#f1f1f1;
  --dark:#1f1f1f;
  --white:#ffffff;
  --hero-a:#6c7a5a;
  --hero-b:#9aa7a0;
}
*{box-sizing:border-box;margin:0;padding:0}
html,body{width:1200px;height:3172px;overflow:hidden}
body{font-family:"Lato",Arial,sans-serif;color:var(--text);background:var(--white);position:relative}
.section-title{font-weight:700;color:var(--ink);font-size:30px;letter-spacing:1px;text-transform:uppercase}
.btn{display:inline-block;font-size:12px;font-weight:700;letter-spacing:1px;text-transform:uppercase;padding:9px 16px;border:1px solid var(--line);color:var(--ink);background:var(--white)}
.btn-orange{background:var(--orange);color:var(--white);border-color:var(--orange)}
p{font-size:14px;line-height:22px}

/* hero */
.hero{position:absolute;top:0;left:0;width:1200px;height:660px;background:linear-gradient(180deg,#4b5b48 0%,var(--hero-a) 35%,var(--hero-b) 65%,#7d7f7c 100%)}
.hero-photo{position:absolute;inset:0;background:radial-gradient(ellipse 420px 200px at 560px 420px,rgba(60,170,90,.55),transparent 70%)}
.nav{position:absolute;top:0;left:0;right:0;height:96px;display:flex;align-items:center;justify-content:space-between;padding:0 72px;background:rgba(0,0,0,.15)}
.brand{font-weight:900;color:var(--white);font-size:22px;letter-spacing:1px;text-transform:uppercase}
.menu{display:flex;gap:6px;list-style:none}
.menu li{font-size:13px;font-weight:700;color:var(--white);padding:12px 16px;text-transform:uppercase}
.menu li.active{background:var(--orange)}
.hero-text{position:absolute;top:280px;width:100%;text-align:center;color:var(--white)}
.hero-text h1{font-size:54px;font-weight:900;line-height:58px;text-transform:uppercase;letter-spacing:1px}
.hero-text .tagline{font-size:30px;font-weight:700;margin-top:8px}
.dots{position:absolute;top:612px;width:100%;display:flex;justify-content:center;gap:10px}
.dots span{width:12px;height:12px;border-radius:50%;background:rgba(255,255,255,.55)}
.dots span.on{background:var(--white)}

/* blog */
.blog{position:absolute;top:700px;left:72px;width:1056px}
.head-row{display:flex;justify-content:space-between;align-items:center;height:64px}
.blog-body{display:flex;gap:60px;margin-top:24px}
.feature{width:516px}
.img{background:linear-gradient(135deg,#8aa6b8,#c7a27c)}
.feature .img{height:244px}
.post-title{color:var(--orange);font-size:14px;font-weight:700;text-transform:uppercase;margin:18px 0 8px}
.meta{font-size:12px;color:var(--muted);margin-top:12px;display:flex;gap:16px;align-items:center}
.meta i{display:inline-block;width:10px;height:10px;background:var(--orange);margin-right:6px}
.side{width:480px;display:flex;flex-direction:column;gap:36px}
.side-item{display:flex;gap:18px}
.side-item .img{width:160px;height:124px;flex:none}
.side-item .post-title{margin-top:0}
.side-item p{font-size:13px;line-height:20px}

/* locations */
.locations{position:absolute;top:1312px;left:0;width:1200px;height:440px;background:linear-gradient(180deg,#1b2535,#2b3a52 60%,#1d2433)}
.locations .section-title{color:var(--white);text-align:center;margin-top:44px}
.cards{position:absolute;top:108px;left:188px;display:flex;gap:36px}
.card{width:240px;height:200px;background:var(--white);padding:8px;position:relative}
.card .img{height:184px}
.card .label{position:absolute;left:8px;right:8px;bottom:8px;height:38px;background:var(--white);color:var(--ink);font-weight:900;font-size:15px;display:flex;align-items:center;justify-content:center;text-transform:uppercase}
.arrow{position:absolute;top:196px}
.locations .btn{position:absolute;top:362px;left:518px;background:transparent;color:var(--white);border-color:rgba(255,255,255,.6)}

/* reviews */
.reviews{position:absolute;top:1790px;left:72px;width:1056px;text-align:center}
.review-cols{display:flex;justify-content:space-between;margin-top:40px;text-align:left}
.review{width:320px}
.stars{color:var(--orange);font-size:18px;letter-spacing:2px}
.stars small{color:var(--text);font-size:13px;letter-spacing:0;margin-left:6px}
.review h3{font-size:14px;color:var(--ink);margin:10px 0 8px;text-transform:uppercase}
.reviewer{color:var(--orange);font-size:13px;margin-top:6px}
.partners{display:flex;justify-content:center;gap:60px;margin-top:40px;align-items:center}
.partner{display:flex;align-items:center;gap:12px;font-size:30px;font-weight:900;color:var(--ink)}
.partner span{width:36px;height:36px;border-radius:50%;background:var(--ink)}
.reviews .btn{margin-top:24px}

/* about */
.about{position:absolute;top:2312px;left:0;width:1200px;height:368px;background:var(--light)}
.about-text{position:absolute;top:52px;left:72px;width:680px}
.about-text p{margin:24px 0 28px}
.portrait{position:absolute;border-radius:50%;border:5px solid var(--white);background:linear-gradient(135deg,#7b5a46,#d8b69c)}

/* contact */
.contact{position:absolute;top:2712px;left:0;width:1200px;text-align:center}
.form{position:absolute;top:72px;left:248px;width:700px;height:180px}
.field{position:absolute;left:0;width:340px;height:52px;border:1px solid var(--line);font-size:13px;color:var(--text);padding:16px;text-align:left}
.field.msg{left:360px;width:340px;height:180px}
.contact .btn-orange{position:absolute;top:276px;left:550px;width:100px;padding:10px 0}

/* footer */
.footer{position:absolute;top:3092px;left:0;width:1200px;height:80px;background:var(--dark);display:flex;align-items:center;justify-content:space-between;padding:0 72px;font-size:12px;color:#aaa}
.social{display:flex;gap:18px}
.social span{width:18px;height:18px;border-radius:50%;background:#777}
</style>
</head>
<body>

<header class="hero">
  <div class="hero-photo" role="img" aria-label="Traveler standing beside a vintage green convertible car on a palm-lined street"></div>
  <nav class="nav">
    <div class="brand">Roads by Her Compass</div>
    <ul class="menu">
      <li class="active">Home</li><li>Blog</li><li>Locations</li><li>Reviews</li><li>About Me</li><li>Contact Us</li>
    </ul>
  </nav>
  <div class="hero-text">
    <h1>Welcome to<br>Roads by Her Compass</h1>
    <div class="tagline">Morbi elementum turpis at pretium venenatis</div>
  </div>
  <div class="dots"><span></span><span class="on"></span><span></span></div>
</header>

<section class="blog">
  <div class="head-row">
    <h2 class="section-title">Blog Posts</h2>
    <span class="btn">View All Posts</span>
  </div>
  <div class="blog-body">
    <article class="feature">
      <div class="img" role="img" aria-label="Group of friends posing together outdoors on a trip"></div>
      <h3 class="post-title">Neque porro quisquam est qui dolorem</h3>
      <p>Phasellus ultrices molestie augue, vitae fermentum turpis varius quisque penatibus et magnis dis parturient montes, nascetur ridiculus mus. Morbi ultrices tincidunt felis, sed lobortis massa posuere quis est lorem.</p>
      <div class="meta"><span><i></i>Posted by Admin</span><span><i></i>05 Comments</span><span><i></i>28 Share</span></div>
    </article>
    <div class="side">
      <article class="side-item">
        <div class="img" role="img" aria-label="Historic building facade"></div>
        <div><h3 class="post-title">Neque porro quisquam est qui</h3>
        <p>Phasellus ultrices molestie augue, vitae fermentum turpis varius quisque penatibus et magnis dis parturient montes.</p>
        <div class="meta"><span><i></i>Posted by Admin</span><span><i></i>05 Comments</span><span><i></i>28 Share</span></div></div>
      </article>
      <article class="side-item">
        <div class="img" role="img" aria-label="Traveler holding a koala"></div>
        <div><h3 class="post-title">Neque porro quisquam est qui</h3>
        <p>Phasellus ultrices molestie augue, vitae fermentum turpis varius quisque penatibus et magnis dis parturient montes.</p>
        <div class="meta"><span><i></i>Posted by Admin</span><span><i></i>05 Comments</span><span><i></i>28 Share</span></div></div>
      </article>
      <article class="side-item">
        <div class="img" role="img" aria-label="Traveler silhouetted at sunset"></div>
        <div><h3 class="post-title">Neque porro quisquam est qui</h3>
        <p>Phasellus ultrices molestie augue, vitae fermentum turpis varius quisque penatibus et magnis dis parturient montes.</p>
        <div class="meta"><span><i></i>Posted by Admin</span><span><i></i>05 Comments</span><span><i></i>28 Share</span></div></div>
      </article>
    </div>
  </div>
</section>

<section class="locations" role="img" aria-label="Night sky with hot air balloons behind the location cards">
  <h2 class="section-title">Locations</h2>
  <svg class="arrow" style="left:40px" width="16" height="24" viewBox="0 0 16 24"><path d="M13 2 3 12l10 10" fill="none" stroke="#fff" stroke-width="3"/></svg>
  <svg class="arrow" style="right:40px" width="16" height="24" viewBox="0 0 16 24"><path d="M3 2l10 10L3 22" fill="none" stroke="#fff" stroke-width="3"/></svg>
  <div class="cards">
    <div class="card"><div class="img" role="img" aria-label="Vienna cityscape" style="background:linear-gradient(160deg,#7aa2cf,#c9b28a)"></div><div class="label">Vienna, Austria</div></div>
    <div class="card"><div class="img" role="img" aria-label="Swiss lakeside town" style="background:linear-gradient(160deg,#6fa0d6,#8a9f7a)"></div><div class="label">Switzerland</div></div>
    <div class="card"><div class="img" role="img" aria-label="Thai temple" style="background:linear-gradient(160deg,#5b8fd0,#c9a05a)"></div><div class="label">Thailand</div></div>
    <div class="card"><div class="img" role="img" aria-label="Tropical beach" style="background:linear-gradient(160deg,#7cc3e8,#e6d6a8)"></div><div class="label">Bahama Shores</div></div>
  </div>
  <span class="btn">View All Locations</span>
</section>

<section class="reviews">
  <h2 class="section-title">Reviews</h2>
  <div class="review-cols">
    <div class="review"><div class="stars">★★★★★<small>5/5</small></div><h3>Neque porro quisquam</h3>
      <p>Phasellus ultrices molestie augue, vitae fermentum turpis varius quisque penatibus et magnis dis parturient montes, nascetur ridiculus mus.</p><div class="reviewer">- Name Heading</div></div>
    <div class="review"><div class="stars">★★★★★<small>5/5</small></div><h3>Neque porro quisquam</h3>
      <p>Phasellus ultrices molestie augue, vitae fermentum turpis varius quisque penatibus et magnis dis parturient montes, nascetur ridiculus mus.</p><div class="reviewer">- Name Heading</div></div>
    <div class="review"><div class="stars">★★★★★<small>5/5</small></div><h3>Neque porro quisquam</h3>
      <p>Phasellus ultrices molestie augue, vitae fermentum turpis varius quisque penatibus et magnis dis parturient montes, nascetur ridiculus mus.</p><div class="reviewer">- Name Heading</div></div>
  </div>
  <div class="partners">
    <div class="partner"><span></span>Wandelquist</div>
    <div class="partner">Quorvo</div>
  </div>
  <span class="btn">View More Reviews</span>
</section>

<section class="about">
  <div class="about-text">
    <h2 class="section-title">About Me</h2>
    <p>Phasellus ultrices molestie augue, vitae fermentum turpis varius quisque penatibus et magnis dis parturient montes, nascetur ridiculus mus. Morbi ultrices tincidunt felis, sed lobortis massa posuere quis. Maecenas non metus nec diam fringilla tempor vel nec quam. Integer hendrerit lorem cursus sapien dignissim, sit condimentum libero scelerisque. Cras condimentum diam justo, eu convallis lorem accumsan at. Vestibulum vel porttitor justo.</p>
    <span class="btn btn-orange">Read More</span>
  </div>
  <div class="portrait" role="img" aria-label="Portrait of the travel blogger" style="left:760px;top:36px;width:220px;height:220px"></div>
  <div class="portrait" role="img" aria-label="Travel snapshot" style="left:952px;top:68px;width:96px;height:96px;background:linear-gradient(135deg,#5c7fa8,#c7a48a)"></div>
  <div class="portrait" role="img" aria-label="Travel snapshot" style="left:940px;top:170px;width:130px;height:130px;background:linear-gradient(135deg,#8a6a58,#e0c2a8)"></div>
</section>

<section class="contact">
  <h2 class="section-title">Contact</h2>
  <div class="form">
    <div class="field" style="top:0">Name</div>
    <div class="field" style="top:64px">Email Address</div>
    <div class="field" style="top:128px">Phone No.</div>
    <div class="field msg" style="top:0">Message</div>
  </div>
  <span class="btn btn-orange">Submit</span>
</section>

<footer class="footer">
  <div>Copyright © 2016, Compass Roads Co. All right reserved</div>
  <div class="social"><span></span><span></span><span></span><span></span><span></span><span></span></div>
</footer>

</body>
</html>
```